Trendy Mindset Image For Personal Growth Tool

This is our third contest on this design and hoping we get the right image! We have a very specific project to hopefully make it easier for designers to create what we are looking for.
We sell card decks that are personal growth tools. Each card in the deck has a weekly action step that brings users closer to fulfilling their potential in targeted areas. We have decks for helping people around leadership, sustainability, couples, parenting, etc. Please check out www.deckleapro.com for more detail on our products.

This particular tool is for Thought Levers. So, something that depicts a mind/brain that is high functioning and powered up. Please see the "image" attachment. We would love to have this image turned into a mind/brain. We included a couple other types of imagery that might look good as well. The image should also say Thought Levers on it and have the image and we have provided some cool font styels that we like.

Target Market(s)

Middle class, trendy, male/female, millennial types... people interested in personal development, spiritual growth, self improvement.

Colors
3176b5
876aae
33a6d7

Requirements
Must have
• This is for the back of the card that is 5 inches tall and 3.5 inches wide. Must be in CMYK for printing. Title "Thought Levers" as well as some type of image depicting a strong mental state (please see attachemnts).
Nice to have
• Clever designs... very strong preference given to anyone who uses the "image" file attached to create their own design of the mind/brain.
Should not have
• Should not have cartoon type images or anything that depicts masculine or feminine. Would like this to appeal to all. Also, please, no straight copies of stock images. Please provide original work or at least something that is not something exactly the same as someone else's work. It can be a base for your work but looking for something original work here.

```html
<!DOCTYPE html>
<html lang="en">
<head>
<meta charset="utf-8">
<title>Thought Levers – Card Back</title>
<link rel="stylesheet" href="https://fonts.googleapis.com/css2?family=Orbitron:wght@600&display=swap">
<style>
  :root {
    --page-bg: #ffffff;
    --card-dark: #18141f;
    --card-glow: #584670;
    --card-mid: #2e2640;
    --brain-violet: #876aae;
    --brain-blue: #3176b5;
    --brain-cyan: #33a6d7;
    --brain-indigo: #5b6fd8;
    --brain-pink: #c77fe6;
    --brain-lilac: #e2d4f4;
    --title-lilac: #c6b5df;
    --title-blue-light: #86a6e8;
    --title-blue-dark: #33508f;
  }
  html, body {
    margin: 0;
    width: 1200px;
    height: 1000px;
    overflow: hidden;
    background: var(--page-bg);
  }
  .canvas {
    position: relative;
    width: 1200px;
    height: 1000px;
  }
  .card-back {
    position: absolute;
    left: 356px;
    top: 127px;
    width: 537px;
    height: 768px;
    box-shadow: 0 0 8px rgba(0,0,0,0.55);
  }
  .card-back svg { display: block; }
  .title-line {
    font-family: "Orbitron", "Eurostile", sans-serif;
    font-weight: 600;
  }
  .title-top { fill: var(--title-lilac); }
  .title-bottom { fill: url(#title-blue); }
</style>
</head>
<body>
<main class="canvas">
  <section class="card-back">
    <svg width="537" height="768" viewBox="0 0 537 768" xmlns="http://www.w3.org/2000/svg">
      <defs>
        <radialGradient id="card-glow" cx="0.32" cy="0.22" r="0.75" gradientTransform="translate(0.32 0.22) rotate(35) scale(1 0.75) translate(-0.32 -0.22)">
          <stop offset="0" stop-color="var(--card-glow)"/>
          <stop offset="0.45" stop-color="var(--card-mid)"/>
          <stop offset="0.8" stop-color="var(--card-dark)"/>
        </radialGradient>
        <radialGradient id="energy-core" cx="0.5" cy="0.5" r="0.5">
          <stop offset="0" stop-color="var(--brain-indigo)"/>
          <stop offset="0.55" stop-color="var(--brain-blue)" stop-opacity="0.85"/>
          <stop offset="0.85" stop-color="var(--brain-violet)" stop-opacity="0.55"/>
          <stop offset="1" stop-color="var(--brain-violet)" stop-opacity="0"/>
        </radialGradient>
        <radialGradient id="energy-cyan" cx="0.5" cy="0.5" r="0.5">
          <stop offset="0" stop-color="var(--brain-cyan)" stop-opacity="0.8"/>
          <stop offset="1" stop-color="var(--brain-cyan)" stop-opacity="0"/>
        </radialGradient>
        <radialGradient id="energy-pink" cx="0.5" cy="0.5" r="0.5">
          <stop offset="0" stop-color="var(--brain-pink)" stop-opacity="0.85"/>
          <stop offset="1" stop-color="var(--brain-pink)" stop-opacity="0"/>
        </radialGradient>
        <radialGradient id="energy-lilac" cx="0.5" cy="0.5" r="0.5">
          <stop offset="0" stop-color="var(--brain-lilac)" stop-opacity="0.8"/>
          <stop offset="1" stop-color="var(--brain-lilac)" stop-opacity="0"/>
        </radialGradient>
        <linearGradient id="title-blue" x1="0" y1="0" x2="0" y2="1">
          <stop offset="0" stop-color="var(--title-blue-light)"/>
          <stop offset="0.55" stop-color="#6a8bd2"/>
          <stop offset="1" stop-color="var(--title-blue-dark)"/>
        </linearGradient>
      </defs>

      <rect class="card-surface" width="537" height="768" fill="url(#card-glow)"/>

      <g class="brain-artwork" role="img" aria-label="Glowing abstract brain made of swirling blue, cyan and violet energy ribbons">
        <ellipse cx="265" cy="290" rx="240" ry="205" fill="url(#energy-core)"/>
        <ellipse cx="330" cy="230" rx="150" ry="110" fill="url(#energy-cyan)"/>
        <ellipse cx="260" cy="350" rx="130" ry="90" fill="url(#energy-pink)"/>
        <ellipse cx="120" cy="275" rx="90" ry="70" fill="url(#energy-lilac)"/>
        <ellipse cx="410" cy="310" rx="80" ry="95" fill="url(#energy-cyan)" opacity="0.6"/>
      </g>

      <text class="title-line title-top" x="46" y="575" font-size="64" textLength="443" lengthAdjust="spacingAndGlyphs">THOUGHT</text>
      <text class="title-line title-bottom" x="44" y="658" font-size="90" textLength="445" lengthAdjust="spacingAndGlyphs">LEVERS</text>
    </svg>
  </section>
</main>
</body>
</html>
```